Meadowlark Dental Letterhead

Please design full color letterhead for meadowlark dental. Letterhead should match the motif of the business card. Print and logo should be confined to a one inch margin on top and bottom. The following info should be included:
Meadowlrk Dental with the tooth logo
Curtis R. Holloway, DDS
Gentle Hands, Bright Smiles Daily
Phone #: 918.555.0147
Address: 24813-C N Sycamore, Larkfield, KS

```html
<!DOCTYPE html>
<html lang="en">
<head>
<meta charset="utf-8">
<title>Meadowlark Dental Letterhead</title>
<link href="https://fonts.googleapis.com/css2?family=Josefin+Slab:wght@400;600&family=Lora:wght@400&family=Open+Sans:wght@700&display=swap" rel="stylesheet">
<style>
  :root {
    --backdrop: #e9e6e1;
    --paper: #ffffff;
    --navy: #1f3f8f;
    --brand-blue: #2d5fb0;
    --accent-red: #e0301e;
    --rule-blue: #2c5bb4;
    --band-green: #3fae3a;
    --ink: #4a4a4a;
  }
  * { box-sizing: border-box; margin: 0; padding: 0; }
  html, body {
    width: 1200px; height: 884px; overflow: hidden;
    background: var(--backdrop);
  }
  .letterhead {
    position: absolute; left: 275px; top: 22px;
    width: 650px; height: 840px;
    background: var(--paper);
    box-shadow: 0 2px 10px rgba(0,0,0,.18);
    overflow: hidden;
  }
  .masthead {
    position: absolute; left: 56px; top: 56px;
    display: flex; align-items: flex-start;
  }
  .brand { padding-right: 14px; }
  .brand-name {
    display: flex; align-items: center; gap: 8px;
    font-family: "Open Sans", sans-serif; font-weight: 700;
    font-size: 17px; line-height: 1.05; color: var(--navy);
    text-transform: uppercase; letter-spacing: .5px;
  }
  .brand-mark {
    width: 34px; height: 34px; border-radius: 50%;
    background: var(--band-green); flex: none;
  }
  .brand-tagline {
    margin-top: 5px; padding-left: 42px;
    font-family: "Open Sans", sans-serif; font-weight: 700;
    font-size: 5.5px; color: var(--navy); text-transform: uppercase;
  }
  .divider { width: 2px; height: 50px; background: var(--accent-red); }
  .contact {
    padding-left: 10px;
    font-family: "Lora", serif; color: var(--brand-blue);
  }
  .contact-name { font-size: 17px; line-height: 1.2; }
  .contact-line {
    display: flex; align-items: center; gap: 5px;
    font-size: 15px; line-height: 1.2;
  }
  .contact-line svg { width: 12px; height: 14px; flex: none; }
  .letter-body {
    position: absolute; left: 86px; right: 86px; top: 188px;
    font-family: "Josefin Slab", serif; font-weight: 600;
    font-size: 11.5px; line-height: 17.5px; color: var(--ink);
    text-align: justify;
  }
  .letter-body p { margin-bottom: 17.5px; }
  .footer {
    position: absolute; left: 0; right: 0; bottom: 0; height: 72px;
  }
  .footer-rule { position: absolute; left: 0; right: 0; height: 4px; }
  .footer-rule--red { top: 0; background: var(--accent-red); }
  .footer-rule--blue { top: 9px; background: var(--rule-blue); }
  .footer-band {
    position: absolute; left: 0; right: 0; bottom: 0; height: 48px;
    background: var(--band-green);
    display: flex; align-items: center; justify-content: flex-end;
    padding-right: 40px;
    font-family: "Open Sans", sans-serif; font-weight: 700;
    font-size: 15px; color: #ffffff;
  }
</style>
</head>
<body>
  <main class="letterhead">
    <header class="masthead">
      <div class="brand">
        <div class="brand-name"><span class="brand-mark"></span><span>Meadowlark<br>Dental</span></div>
        <div class="brand-tagline">Gentle Hands, Bright Smiles Daily</div>
      </div>
      <div class="divider"></div>
      <div class="contact">
        <div class="contact-name">Curtis R. Holloway, DDS</div>
        <div class="contact-line">
          <svg viewBox="0 0 12 14" aria-hidden="true"><path d="M6 1a4 4 0 0 0-4 4c0 3 4 8 4 8s4-5 4-8a4 4 0 0 0-4-4zm0 5.6a1.6 1.6 0 1 1 0-3.2 1.6 1.6 0 0 1 0 3.2z" fill="none" stroke="currentColor" stroke-width="1.3"/></svg>
          <span>24813-C N Sycamore, Larkfield, KS</span>
        </div>
        <div class="contact-line">
          <svg viewBox="0 0 12 14" aria-hidden="true"><path d="M1 6c0-2 2-3 5-3s5 1 5 3H8.5V5h-5v1zM2.5 7h7l1 5h-9z" fill="currentColor"/></svg>
          <span># 918.555.0147</span>
        </div>
      </div>
    </header>

    <section class="letter-body">
      <p>Lorem ipsum dolor sit amet,</p>
      <p>Lorem ipsum dolor sit amet, consectetur adipiscing elit. Donec orci purus, luctus vitae dignissim eu, iaculis sed purus. Vivamus faucibus, ipsum nec aliquet viverra, leo mauris condimentum ligula, sit amet sagittis enim ligula quis arcu. Nam egestas tortor id nisi porttitor mattis. In tortor ante, ultricies in suscipit a, tempus non massa. Vivamus et auctor mi. Fusce vel massa nulla. Phasellus nec eros mauris, et scelerisque orci. Donec malesuada orci vitae nulla accumsan porta a id massa. Quisque accumsan iaculis magna sit amet fringilla. Maecenas consequat, magna eget tincidunt semper, odio nibh rutrum mi, id feugiat ante nisi eu risus. Vestibulum nunc orci, rhoncus a placerat in, ultricies in mi. Cras mattis varius eros, vel fringilla nisi suscipit eget.</p>
      <p>Quisque scelerisque sagittis nulla at porttitor. Mauris a justo et tellus interdum tristique. Sed id augue vitae urna euismod commodo aliquet a quam. Pellentesque arcu velit, cursus et malesuada ut, consequat et diam. Nullam erat sem, rhoncus id ullamcorper vitae, rhoncus et arcu. In ultricies ultricies nulla, ut rutrum nisi iaculis at. Donec eu magna a metus ornare faucibus. Fusce aliquet faucibus ultricies. Morbi semper, est id tincidunt gravida, eros arcu adipiscing lacus, ac bibendum nulla leo eu purus. Quisque nec diam sed risus consectetur accumsan quis quis nibh. Vestibulum id purus lorem.</p>
      <p>Vivamus vehicula accumsan lacinia. Aliquam erat volutpat. Pellentesque consequat venenatis velit non gravida. Etiam et sem et nulla congue aliquam sed eget augue. Nulla facilisi. Pellentesque habitant morbi tristique senectus et netus et malesuada fames ac turpis egestas. Nulla a elit at sem iaculis congue. Nullam mollis tristique lobortis.</p>
    </section>

    <footer class="footer">
      <div class="footer-rule footer-rule--red"></div>
      <div class="footer-rule footer-rule--blue"></div>
      <div class="footer-band">Caring For Every Family Smile</div>
    </footer>
  </main>
</body>
</html>
```